Elegant, Playful, Health And Wellness Packaging Design for an Essential Oil Diffuser

Box design for diffuser, should be elegant, luxury, white box with gold foil and vibrant color combination that pops off the white box.

Designs look the same

```html
<!DOCTYPE html>
<html lang="en">
<head>
<meta charset="utf-8">
<title>LUMA Ultrasonic Diffuser – Box Panels</title>
<link rel="stylesheet" href="https://fonts.googleapis.com/css2?family=Playfair+Display:wght@800&family=Lato:wght@400;700&family=Oswald:wght@300&display=swap">
<style>
  :root {
    --page: #ffffff;
    --panel: #f4f4f4;
    --pattern: #e7e7e7;
    --ink: #1c1c1c;
    --red: #b8202e;
    --gold-dark: #7a6249;
    --gold-mid: #a8916f;
    --gold-light: #d3bc94;
    --gold-text: #5e4a36;
  }
  * { margin: 0; padding: 0; box-sizing: border-box; }
  html, body { width: 1200px; height: 1200px; overflow: hidden; background: var(--page); }
  .canvas { position: relative; width: 1200px; height: 1200px; }

  .box { position: absolute; top: 290px; left: 70px; display: flex; height: 620px;
         box-shadow: 0 18px 40px rgba(0,0,0,0.08); }
  .panel { position: relative; height: 100%; background: var(--panel); overflow: hidden; }
  .panel--side { width: 360px; border-right: 1px solid #e2e2e2; }
  .panel--front { width: 700px; }

  .pattern { position: absolute; left: 0; top: 0; right: 0; height: 73%; background: var(--pattern); opacity: .55; }

  .red-line { position: absolute; left: 0; right: 0; top: 73%; height: 9px; background: var(--red); }
  .gold-band { position: absolute; left: 0; right: 0; top: 76.5%; bottom: 0;
               background: linear-gradient(90deg, var(--gold-dark), var(--gold-mid) 45%, var(--gold-light)); }
  .panel--side .gold-band { background: linear-gradient(90deg, #6f5842, var(--gold-dark)); }

  .side-copy { position: absolute; left: 48px; top: 130px; width: 270px;
               font-family: 'Oswald', sans-serif; font-weight: 300; font-size: 12.5px;
               line-height: 1.55; color: #333; }
  .side-copy .heading { display: block; }

  .brand { position: absolute; left: 0; right: 0; top: 62px; text-align: center;
           font-family: 'Playfair Display', serif; font-weight: 800; font-size: 104px;
           letter-spacing: 2px; color: var(--ink); line-height: 1; }
  .collection { position: absolute; left: 0; right: 0; top: 186px; text-align: center;
                font-family: 'Lato', sans-serif; font-size: 23px; letter-spacing: 3px; color: var(--ink); }
  .tagline { position: absolute; left: 0; right: 0; top: 236px; text-align: center;
             font-family: 'Lato', sans-serif; font-size: 15px; letter-spacing: 1.5px; color: var(--ink); }

  .seal { position: absolute; left: 50%; top: 400px; transform: translateX(-50%);
          display: flex; flex-direction: column; align-items: center; gap: 10px; }
  .seal-dot { width: 120px; height: 120px; border-radius: 50%;
              background: linear-gradient(135deg, var(--gold-light), var(--gold-mid)); }
  .seal-name { font-family: 'Lato', sans-serif; font-weight: 700; font-size: 13px;
               letter-spacing: 3px; color: var(--gold-text); white-space: nowrap; }

  .product-type { position: absolute; left: 0; right: 0; bottom: 26px; text-align: center;
                  font-family: 'Lato', sans-serif; font-size: 15px; letter-spacing: 3px; color: var(--gold-text); }
</style>
</head>
<body>
<main class="canvas">
  <div class="box">
    <section class="panel panel--side">
      <div class="pattern" role="img" aria-label="Faint grey zigzag background pattern"></div>
      <p class="side-copy">
        <span class="heading">Heading: VELVET GROVE ESSENTIAL OILS DIFFUSER</span>
        Experience the pure essence of nature with the Rare Oils Luma Diffuser. Sourced from the farthest reaches of the earth, Velvet Grove Oils are extracted only from the highest quality and purest raw form ingredients. Using the Luma diffuser with Velvet Grove Oils can help improve health, quality of life, and overall spiritual balance.
      </p>
      <div class="red-line"></div>
      <div class="gold-band"></div>
    </section>

    <section class="panel panel--front">
      <div class="pattern" role="img" aria-label="Faint grey zigzag background pattern"></div>
      <h1 class="brand">LUMA</h1>
      <p class="collection">Signature Rare Oils Collection</p>
      <p class="tagline">EXPERIENCE THE ESSENCE OF NATURE</p>
      <div class="red-line"></div>
      <div class="gold-band"></div>
      <div class="seal">
        <span class="seal-dot"></span>
        <span class="seal-name">VELVET GROVE</span>
      </div>
      <p class="product-type">ULTRASONIC DIFFUSER</p>
    </section>
  </div>
</main>
</body>
</html>
```